Our desktop web app builder needs a redesign

We want to redesign our low-code web app builder called Fernhold. Fernhold runs in desktop environments and is aimed at IT professionals and developers.

The UI consists of a button bar, multiple panels and a tabbed working area. We are looking to completely change the look and feel of the application interfaces, while keeping the layout and functionality the same.

We would like to see your ideas for fonts, sizing, colour, icons and any other visual UI element. Your work can be a rough mockup of your design ideas, and does not need to be pixel perfect. Legibility and optimised use of space are key.

More details about the app and how it works here: https://fernhold.software/

If we like your ideas, we will get in touch with you and work with you to develop the new design in greater detail.

```html
<!DOCTYPE html>
<html lang="en">
<head>
<meta charset="utf-8">
<title>Fernhold – Columns</title>
<link rel="stylesheet" href="https://fonts.googleapis.com/css2?family=Mulish:wght@400;600;700&display=swap">
<style>
  :root {
    --brand: #00b4d3;
    --brand-soft: #a6e3ee;
    --surface: #f0f3f6;
    --surface-footer: #f4f6f8;
    --white: #ffffff;
    --rule: #c9cbcd;
    --text: #4a4a4a;
    --text-strong: #3f4245;
    --text-muted: #5a5d60;
  }
  * { box-sizing: border-box; margin: 0; padding: 0; }
  html, body { width: 1200px; height: 780px; overflow: hidden; background: var(--white); }
  body { font-family: "Mulish", Arial, sans-serif; color: var(--text); }

  .dialog { position: relative; width: 1200px; height: 780px; background: var(--surface); }
  .dialog-header { position: absolute; left: 0; top: 0; width: 1200px; height: 60px; background: var(--brand); }
  .dialog-title { position: absolute; left: 26px; top: 14px; font-size: 24px; font-weight: 700; color: var(--white); }
  .header-icon { position: absolute; top: 19px; }
  .icon-maximize { left: 1111px; }
  .icon-close { left: 1153px; }

  .sidebar { position: absolute; left: 0; top: 60px; width: 355px; height: 655px; border-right: 2px solid var(--rule); }
  .sidebar-item { position: absolute; left: 0; width: 355px; height: 58px; line-height: 58px; padding-left: 31px; font-size: 19px; color: var(--text-muted); }
  .sidebar-item.is-selected { background: var(--brand-soft); font-weight: 700; color: var(--text-strong); }

  .section-title { position: absolute; left: 377px; font-size: 21px; font-weight: 700; color: var(--text-strong); }
  .section-desc { position: absolute; left: 377px; top: 143px; font-size: 18px; color: var(--text-muted); }
  .divider { position: absolute; left: 377px; width: 801px; height: 2px; background: var(--rule); }

  .field-label { position: absolute; left: 377px; font-size: 19px; color: var(--text-muted); line-height: 24px; }
  .field-box { position: absolute; left: 558px; width: 473px; height: 32px; background: var(--white); border: 1.5px solid var(--brand); font-size: 19px; line-height: 29px; padding-left: 8px; color: var(--text); }
  .field-button { position: absolute; left: 1031px; width: 35px; height: 32px; background: var(--brand); display: flex; align-items: center; justify-content: center; }
  .expr-mark { position: absolute; right: 8px; top: 0; font-weight: 700; font-size: 18px; color: var(--text-strong); }
  .expr-mark sup, .option sup { font-size: 11px; }

  .event-link { position: absolute; left: 566px; top: 412px; font-size: 19px; color: var(--text-muted); text-decoration: underline; text-underline-offset: 4px; }

  .dropdown { position: absolute; left: 558px; top: 536px; width: 508px; height: 143px; background: var(--white); border: 1.5px solid var(--brand); border-top: none; overflow: hidden; }
  .option { position: absolute; left: 0; width: 486px; height: 36px; line-height: 36px; font-size: 19px; color: var(--text); display: flex; align-items: center; }
  .option.is-active { background: var(--brand-soft); }
  .option-caret { width: 0; height: 0; border-left: 6px solid transparent; border-right: 6px solid transparent; border-top: 8px solid var(--brand); margin-right: 9px; }
  .scrollbar { position: absolute; right: 0; top: 0; width: 20px; height: 143px; border-left: 1.5px solid var(--brand); }
  .scrollbar-thumb { position: absolute; left: 2px; top: 21px; width: 16px; height: 27px; background: var(--brand-soft); }

  .dialog-footer { position: absolute; left: 0; top: 715px; width: 1200px; height: 65px; background: var(--surface-footer); border-top: 1.5px solid var(--rule); }
  .add-column { position: absolute; left: 27px; top: 20px; display: flex; align-items: center; font-size: 22px; color: var(--text-muted); }
  .add-column svg { margin-right: 12px; }
  .delete-column { position: absolute; left: 315px; top: 21px; }
  .btn { position: absolute; top: 17px; height: 34px; width: 125px; font-family: inherit; font-size: 18px; display: flex; align-items: center; justify-content: center; }
  .btn-primary { left: 906px; background: var(--brand); color: var(--white); border: none; }
  .btn-secondary { left: 1048px; background: var(--white); color: var(--text-strong); border: 1.5px solid var(--brand); }
</style>
</head>
<body>
<div class="dialog">
  <header class="dialog-header">
    <h1 class="dialog-title">Columns</h1>
    <svg class="header-icon icon-maximize" width="21" height="21" viewBox="0 0 21 21"><rect x="1.5" y="1.5" width="18" height="18" fill="none" stroke="#fff" stroke-width="3"/></svg>
    <svg class="header-icon icon-close" width="21" height="21" viewBox="0 0 21 21"><path d="M2 2L19 19M19 2L2 19" stroke="#fff" stroke-width="4" stroke-linecap="round"/></svg>
  </header>

  <nav class="sidebar">
    <div class="sidebar-item is-selected" style="top:48px">FirstName</div>
    <div class="sidebar-item" style="top:106px">LastName</div>
    <div class="sidebar-item" style="top:164px">Age</div>
    <div class="sidebar-item" style="top:222px">Height</div>
  </nav>

  <h2 class="section-title" style="top:102px">Column Type</h2>
  <p class="section-desc">Choose whether the cell displays a value from a connector or the specified text</p>
  <div class="divider" style="top:185px"></div>

  <span class="field-label" style="top:220px">Column Type</span>
  <div class="field-box" style="top:216px">Data Bound</div>
  <div class="field-button" style="top:216px">
    <svg width="16" height="10" viewBox="0 0 16 10"><path d="M2 2L8 8L14 2" fill="none" stroke="#fff" stroke-width="2.5"/></svg>
  </div>

  <span class="field-label" style="top:268px">Text</span>
  <div class="field-box" style="top:264px">(Data Bound)</div>
  <div class="divider" style="top:325px"></div>

  <h2 class="section-title" style="top:362px">Events</h2>
  <span class="field-label" style="top:412px">Click</span>
  <span class="event-link">CreateEventHandler</span>
  <div class="divider" style="top:472px"></div>

  <span class="field-label" style="top:508px">Header Text</span>
  <div class="field-box" style="top:504px">First Name<span class="expr-mark">X<sup>2</sup></span></div>
  <div class="field-button" style="top:504px">
    <svg width="16" height="10" viewBox="0 0 16 10"><path d="M2 8L8 2L14 8" fill="none" stroke="#fff" stroke-width="2.5"/></svg>
  </div>

  <span class="field-label" style="top:556px">Alignment</span>
  <span class="field-label" style="top:604px">Cel Display</span>
  <span class="field-label" style="top:652px">Visible</span>

  <div class="dropdown" role="listbox">
    <div class="option" style="top:0;padding-left:19px"><b style="margin-right:3px">X<sup>2</sup></b>Expression</div>
    <div class="option" style="top:36px;padding-left:22px"><span class="option-caret"></span>Session</div>
    <div class="option is-active" style="top:72px;padding-left:50px"><span class="option-caret"></span>Logged In User</div>
    <div class="option" style="top:108px;padding-left:106px">ID</div>
    <div class="scrollbar"><div class="scrollbar-thumb"></div></div>
  </div>

  <footer class="dialog-footer">
    <div class="add-column">
      <svg width="20" height="20" viewBox="0 0 20 20"><rect width="20" height="20" rx="2" fill="var(--brand)"/><path d="M10 4.5V15.5M4.5 10H15.5" stroke="#fff" stroke-width="3"/></svg>
      Add Column
    </div>
    <svg class="delete-column" width="20" height="22" viewBox="0 0 20 22"><path d="M1 4H19M7 4V1.5H13V4M3.5 4L4.5 20.5H15.5L16.5 4M8 8V17M12 8V17" fill="none" stroke="var(--brand)" stroke-width="1.8"/></svg>
    <button class="btn btn-primary">SAVE</button>
    <button class="btn btn-secondary">CANCEL</button>
  </footer>
</div>
</body>
</html>
```